Design an Outstanding flyer for my company.

I need a flyer designed for our window tinting company based in Brisbane Queensland Australia. The flyer will be targeting Home tinting. We also do mobile car tinting. Something in regards to this could be incorporated into the flyer as well.
I want it to be 2 sided DL size. Black background.
It really needs to Pop, and be a real attention getter.
It needs to be easy to read.
I have provided a mock up with the info on it from our marketing company. It will need a spellcheck etc to make sure everything is correct.
Everything about it can be changed however you like.
I have also included the company logo.

Lets see what you've got!

Target Market(s)

Home Owners

Industry/Entity Type

Home Improvement

Font styles to use
Other font styles liked:
• Duan Penh

Requirements
Must have
• All the information on the mock up. Clear and easy to read.
• Must Stand Out!

```html
<!DOCTYPE html>
<html lang="en">
<head>
<meta charset="utf-8">
<title>Brightline Tinting – DL Flyer</title>
<link rel="stylesheet" href="https://fonts.googleapis.com/css2?family=Roboto:ital,wght@0,400;0,500;0,700;0,900;1,700&family=Source+Sans+3:wght@300;400&display=swap">
<style>
  :root {
    --ink: #1f1e1f;
    --gold: #f9c623;
    --white: #ffffff;
    --stage: #e6e6e6;
    --photo-warm: #6b4a33;
    --photo-sky: #9fb8cc;
    --photo-wood: #8a4f26;
  }
  * { box-sizing: border-box; margin: 0; padding: 0; }
  html, body { width: 1200px; height: 788px; overflow: hidden; }
  body {
    background: var(--stage);
    font-family: "Roboto", Arial, sans-serif;
    position: relative;
  }
  .flyer {
    position: absolute;
    background: var(--ink);
    overflow: hidden;
    color: var(--white);
  }
  .flyer--front { left: 144px; top: 67px; width: 431px; height: 611px; }
  .flyer--back  { left: 628px; top: 67px; width: 436px; height: 617px; }

  /* Photo areas */
  .photo { position: absolute; left: 0; top: 0; width: 100%; }
  .flyer--front .photo {
    height: 310px;
    background:
      linear-gradient(to bottom, rgba(31,30,31,0) 60%, var(--ink) 100%),
      linear-gradient(to bottom, var(--photo-warm) 0%, var(--photo-sky) 35%, #a58a6e 55%, #6d6b6c 80%);
  }
  .flyer--back .photo {
    height: 245px;
    background:
      linear-gradient(to bottom, rgba(31,30,31,0) 55%, var(--ink) 100%),
      linear-gradient(to right, var(--photo-wood) 0%, #c9c9c4 30%, #b5b8b6 70%, var(--photo-wood) 100%);
  }

  /* Front */
  .top-banner {
    position: absolute; left: 0; top: 11px;
    width: 408px; height: 32px;
    background: var(--gold);
    clip-path: polygon(0 0, 100% 0, 94% 100%, 0 100%);
    color: var(--ink);
    font-weight: 700; font-size: 17px;
    line-height: 32px; padding-left: 15px;
    letter-spacing: 0.1px;
  }
  .compare-tag {
    position: absolute;
    background: var(--gold); color: var(--ink);
    font-family: "Source Sans 3", Arial, sans-serif;
    font-size: 14px; line-height: 18px; padding: 0 4px;
  }
  .compare-tag--before { left: 133px; top: 146px; }
  .compare-tag--after  { left: 308px; top: 143px; }

  .headline {
    position: absolute; left: 0; width: 100%; text-align: center;
    font-weight: 700; line-height: 1;
  }
  .headline--main { top: 308px; font-size: 44px; color: var(--gold); }
  .headline--sub  { top: 355px; font-size: 31px; color: var(--white); }

  .dotted-box {
    position: absolute;
    border: 2px dotted var(--gold);
    text-align: center;
  }
  .benefit-box { left: 36px; top: 393px; width: 356px; height: 79px; padding-top: 7px; }
  .benefit {
    font-family: "Source Sans 3", Arial, sans-serif;
    font-weight: 300; font-size: 29px; line-height: 32px;
  }
  .benefit--gold { color: var(--gold); }

  .brand {
    position: absolute; left: 0; width: 100%;
    display: flex; justify-content: center; align-items: center; gap: 10px;
  }
  .brand-dot { width: 28px; height: 28px; border-radius: 50%; background: var(--gold); }
  .brand-name {
    font-weight: 500; font-size: 26px; color: var(--gold);
    letter-spacing: 1px;
  }
  .flyer--front .brand { top: 527px; }
  .flyer--back .brand { top: 532px; }

  .web {
    position: absolute; left: 0; top: 591px; width: 100%;
    text-align: center; font-size: 11px; letter-spacing: 1.5px; color: #ddd;
  }

  /* Back */
  .roll-inset {
    position: absolute; left: 311px; top: 160px; width: 93px; height: 93px;
    border-radius: 50%; border: 3px solid var(--gold);
    background: linear-gradient(135deg, #d9d9d9, #3a3a3a 55%, #9a9a9a);
  }
  .reasons-box { left: 32px; top: 250px; width: 400px; height: 56px; padding-top: 6px; }
  .reasons-title {
    color: var(--gold); font-weight: 700; font-size: 18px; line-height: 21px;
  }
  .reasons {
    position: absolute; left: 28px; top: 327px; width: 382px;
    text-align: center; font-weight: 700; font-size: 11px; line-height: 13px;
    text-transform: uppercase;
  }
  .reasons .hl { color: var(--gold); }
  .call-band {
    position: absolute; left: 0; top: 453px; width: 100%; height: 32px;
    background: var(--gold); color: var(--ink);
    font-weight: 700; font-style: italic; font-size: 14px;
    line-height: 32px; text-align: center;
  }
  .contact {
    position: absolute; left: 0; top: 490px; width: 100%;
    text-align: center; font-weight: 700; font-style: italic; font-size: 17px;
  }
  .contact .label { color: var(--gold); }
  .contact .gap { display: inline-block; width: 12px; }
</style>
</head>
<body>

<section class="flyer flyer--front">
  <div class="photo" role="img" aria-label="Living room with tinted panoramic windows overlooking red rock hills, three silver luxury cars in front"></div>
  <div class="top-banner">PERFECT HOME AND CAR WINDOW TINTING</div>
  <span class="compare-tag compare-tag--before">Before</span>
  <span class="compare-tag compare-tag--after">After</span>

  <h1 class="headline headline--main">KEEP HEAT OUT</h1>
  <h2 class="headline headline--sub">BLOCK 99.9% UV RAYS</h2>

  <div class="dotted-box benefit-box">
    <p class="benefit benefit--gold">SAVE MONEY</p>
    <p class="benefit">INCREASE PRIVACY</p>
  </div>

  <div class="brand">
    <span class="brand-dot"></span>
    <span class="brand-name">BRIGHTLINE TINTING</span>
  </div>
  <p class="web">www.brightlinetinting.com.au</p>
</section>

<section class="flyer flyer--back">
  <div class="photo" role="img" aria-label="Installer applying window film to a large wood-framed window"></div>
  <div class="roll-inset" role="img" aria-label="Rolls of tinting film"></div>

  <div class="dotted-box reasons-box">
    <h2 class="reasons-title">20 REASONS WHY HOME WINDOW TINTING<br>IS PERFECT FOR YOU.</h2>
  </div>

  <p class="reasons">
    Reduce glare. <span class="hl">Reduce energy costs.</span> Control the amount of light entering your home. <span class="hl">Reduce carbon footprint.</span> Make home more beautiful. <span class="hl">Eliminate home hot spots.</span> Protect against broken glass. <span class="hl">Regulate energy.</span> Protects upholstery. <span class="hl">Improve effectiveness of roof insulation.</span> Improve health. <span class="hl">Reduces interior floor fading.</span> Eliminate need for blinds. <span class="hl">Strengthen your windows.</span> Insulate in winter. <span class="hl">Affordable.</span>
  </p>

  <div class="call-band">CALL BRISBANE’S LEADER IN HOME WINDOW TINTING NOW.</div>
  <p class="contact"><span class="label">TEL</span> : 07 3000 1234<span class="gap"></span><span class="label">SMS</span>: 0400 000 123</p>

  <div class="brand">
    <span class="brand-dot"></span>
    <span class="brand-name">BRIGHTLINE TINTING</span>
  </div>
</section>

</body>
</html>
```